Exciting New Reseller Brand requires Website to WOW New clients to register.

We are a NEW online business called Trade Your Goods.

The Website is a simple concept, it looks to put Merchants (businesses that want their products resold) in touch with Resellers (people or businesses that want to resell that product).

The website acts as an online market place which looks to get Merchants to sign-up and pay to list their company and product as well as getting Resellers to sign-up to view potential Merchants they can get in touch with in the right industry or area to resell their products for (see attached slide-pack to explain packages)

Any type of Industry or Business can register themselves to get listed on Trade Your Goods to see either get their product/service resold or to look for products / services to reseller.

Trade Your Goods does not take any other monetary part in the business relationships other than to obtain money for the monthly website subscription.

We want a very simple website, so this project is for several pages:

Page 1) A really vibrant, exciting, image based homepage to get people to sign-up / register (see sites that we like in the project brief). Needs to be very clear that there are 2 customers and to sign up to join, build and earn!

Page 2) A page that describes the benefits and packages for Resellers.

Page 3) A page that describes the benefits and packages for Merchants.

Page 4) The Payment process pages, taking the customer through sign-up

Page 5) The Business Listings page, so when people search for a Merchant how this will be displayed.

We would really like an image based site and preferably parallax. We want it bright vibrant and to look like a social media site.

All necessary files / logos enclosed.

We would love to continue to work with the winning designer moving forward.

Many thanks and Good Luck.

Regards

Martin & Owen

Target Market(s)

Merchants, Suppliers, Vendors, Manufacturers, Distributors, Wholesalers, Affiliate programs, Franchisees, Reselers

Industry/Entity Type

Business

Number of Pages Required

5+ page

Requirements
Must have
• We love the following websites:
• 1) Like the top section, i.e. parallax image based: www.brightfoxstudio.co.uk
• 2) Like the way the screen is split in 2, could be used to describe the 2 different customers we are after Merchants / Resellers: www.cloudtrunk.example/guide
• 3) Like the bright colours / full screen video split into 2 below top banner and the generally how simple the site is: www.harbourlinden.com.au
• 4) Love all of this site, simple, bold, Love the colours, the clear message and the infographics: http://www.velomiro.example/swiftride/quicker

```html
<!DOCTYPE html>
<html lang="en">
<head>
<meta charset="utf-8">
<title>Trade Your Goods — Building Your Own Virtual Sales Team</title>
<link href="https://fonts.googleapis.com/css2?family=Montserrat:wght@400;500;600;700&display=swap" rel="stylesheet">
<style>
:root{
  --green:#9dc63c;
  --green-dark:#6e8f22;
  --blue:#1a8ad2;
  --blue-dark:#0d5f97;
  --ink:#111;
  --night:#050909;
  --night-2:#0b1414;
  --white:#fff;
  --grey:#555;
  --paper:#f7f7f7;
  --red:#d11b1b;
  --purple:#d215c8;
  --chart-blue:#2a7fc8;
  --chart-green:#c8d83a;
}
*{margin:0;padding:0;box-sizing:border-box}
html,body{width:1200px;height:3515px;overflow:hidden}
body{font-family:'Montserrat',Arial,sans-serif;color:var(--ink);background:var(--white);position:relative}
.band{position:absolute;left:0;width:1200px}

/* Hero */
.hero{top:0;height:585px;overflow:hidden;background:#0c0c0c}
.hero-photo{position:absolute;inset:0;background:radial-gradient(ellipse at 50% 40%,#5a5a5a 0%,#2a2a2a 40%,#0c0c0c 80%)}
.brand{position:absolute;top:22px;left:45px;display:flex;align-items:center;gap:10px;color:var(--white);font-weight:700;font-size:24px;letter-spacing:-.3px}
.brand-dot{width:28px;height:28px;border-radius:50%;background:var(--green)}
.main-nav{position:absolute;top:40px;right:50px;display:flex;gap:40px;align-items:center;font-size:14px;font-weight:700;color:var(--white)}
.main-nav .active{color:var(--green)}
.pill{border:2px solid var(--blue);border-radius:20px;padding:5px 16px;color:var(--white)}
.hero-copy{position:absolute;top:225px;left:0;width:1200px;text-align:center}
.hero-kicker{color:var(--green);font-size:25px;letter-spacing:2px;font-weight:500}
.hero-title{color:var(--blue);font-size:60px;font-weight:700;letter-spacing:1px;line-height:1.1}
.hero-rule{width:690px;height:1px;background:rgba(255,255,255,.5);margin:6px auto 10px}
.hero-tag{color:var(--white);font-size:36px;font-weight:600;letter-spacing:3px}
.dots{position:absolute;top:418px;left:575px;display:flex;gap:6px}
.dots span{width:10px;height:10px;border-radius:50%;background:var(--white)}
.dots span.off{background:#777}

/* Split */
.split{top:585px;height:587px;display:flex}
.split-half{width:600px;height:587px;color:var(--white);text-align:center;padding-top:70px}
.split-half.resellers{background:var(--green)}
.split-half.merchants{background:var(--blue)}
.split-title{font-size:42px;font-weight:600;letter-spacing:1px}
.split-sub{font-size:17px;font-weight:600;margin-top:2px}
.split-lead{font-size:20px;font-weight:600;color:#1e2a10;margin-top:18px;line-height:1.2}
.merchants .split-lead{color:#0b2740}
.split-list{list-style:none;margin-top:24px;font-size:17px;font-weight:600;line-height:24.5px}
.btn{display:inline-block;width:155px;height:36px;line-height:36px;border-radius:18px;font-size:14px;font-weight:700;color:var(--white);text-align:center}
.resellers .btn{background:#5d7a1c;margin-top:40px}
.merchants .btn{background:var(--blue-dark);margin-top:40px}

/* Why */
.why{top:1172px;height:603px;background:var(--white);overflow:hidden}
.why-photo{position:absolute;right:0;top:0;width:700px;height:603px;background:linear-gradient(90deg,#fff 0%,#c9d7e4 25%,#6f93b5 55%,#2a3c55 100%)}
.why-copy{position:absolute;left:50px;top:80px}
.why-title{color:var(--green);font-size:40px;font-weight:600;letter-spacing:1px}
.why-pre{font-size:18px;color:#333;margin-top:14px}
.why-big{color:var(--blue);font-size:44px;font-weight:600;letter-spacing:1px;line-height:1.1}
.why-list{list-style:none;margin-top:16px;font-size:18px;color:#333}
.why-list li{height:40px;display:flex;align-items:center;gap:14px}
.why-list li::before{content:"";width:12px;height:12px;border:2px solid var(--green);border-radius:50%}
.why .btn{background:var(--blue);width:182px;margin-top:32px}

/* Growth */
.growth{top:1775px;height:585px;background:linear-gradient(180deg,var(--night),var(--night-2))}
.growth-title{position:absolute;top:70px;width:1200px;text-align:center;color:var(--white);font-size:36px;font-weight:600;letter-spacing:1px}
.growth-title span{color:var(--green)}
.growth svg{position:absolute;left:0;top:0}

/* How */
.how{top:2360px;height:565px;background:var(--paper)}
.how-title{position:absolute;top:62px;width:1200px;text-align:center;font-size:36px;font-weight:600;color:#111;letter-spacing:1px}
.how-title span{color:var(--green)}
.flow{position:absolute;left:50px;width:1100px;height:139px;border-radius:8px;display:flex;align-items:center;padding:0 38px;color:var(--white);font-size:28px;font-weight:500}
.flow.merchant-flow{top:137px;background:var(--blue)}
.flow.reseller-flow{top:293px;background:var(--green)}
.flow .bullet{width:30px;height:30px;border-radius:50%;border:5px solid var(--white);margin-right:18px}
.flow .arrow{margin:0 14px 0 24px}
.flow .pricing{margin-left:auto;width:155px;height:36px;line-height:36px;text-align:center;border-radius:18px;font-size:14px;font-weight:700}
.merchant-flow .pricing{background:var(--blue-dark)}
.reseller-flow .pricing{background:#6d8c25}
.shadow{position:absolute;left:80px;top:490px;width:1040px;height:30px;border-radius:50%;background:radial-gradient(ellipse,rgba(0,0,0,.28),rgba(0,0,0,0) 70%)}

/* Footer */
.footer-nav{top:2925px;height:113px;background:#000;display:flex;justify-content:center;align-items:center;gap:50px;font-size:14px;font-weight:700;color:var(--white)}
.footer-nav .active{color:var(--green)}
.site-footer{top:3038px;height:477px;background:linear-gradient(180deg,#071010,#030707);color:var(--white);text-align:center}
.footer-brand{position:absolute;top:80px;left:0;width:1200px;display:flex;justify-content:center;align-items:center;gap:10px;font-size:28px;font-weight:700}
.footer-blurb{position:absolute;top:155px;left:270px;width:660px;font-size:12px;line-height:16px}
.copyright{position:absolute;top:268px;width:1200px;font-size:12px}
.socials{position:absolute;top:315px;left:0;width:1200px;display:flex;justify-content:center;gap:14px}
.socials span{width:32px;height:32px;border-radius:50%;background:var(--white)}
.legal{position:absolute;top:376px;width:1200px;display:flex;justify-content:center;gap:16px;font-size:12px;font-weight:600}
</style>
</head>
<body>

<header class="band hero">
  <div class="hero-photo" role="img" aria-label="Dark photo of a connected network of business people figures"></div>
  <div class="brand"><span class="brand-dot"></span>tradeyourgoods</div>
  <nav class="main-nav">
    <span class="active">HOME</span><span>RESELLERS</span><span>MERCHANTS</span><span>BUSINESS LISTINGS</span><span class="pill">SIGN-UP</span>
  </nav>
  <div class="hero-copy">
    <div class="hero-kicker">BUILDING YOUR OWN</div>
    <div class="hero-title">VIRTUAL SALES TEAM</div>
    <div class="hero-rule"></div>
    <div class="hero-tag">JOIN - BUILD - EARN</div>
  </div>
  <div class="dots"><span></span><span></span><span class="off"></span><span></span></div>
</header>

<section class="band split">
  <div class="split-half resellers">
    <div class="split-title">RESELLERS</div>
    <div class="split-sub">Benefits And Packages</div>
    <div class="split-lead">GROW BUSINESS &amp;<br>INCREASE SALES</div>
    <ul class="split-list">
      <li>Products</li><li>Suppliers</li><li>Vendors</li><li>Manufacturers</li><li>Distributors</li><li>Wholesalers</li><li>Affiliate programs</li><li>Franchise</li>
    </ul>
    <span class="btn">SIGN UP</span>
  </div>
  <div class="split-half merchants">
    <div class="split-title">MERCHANTS</div>
    <div class="split-sub">Benefits And Packages</div>
    <div class="split-lead">GROW PORTFOLIO &amp;<br>INCREASE INCOME</div>
    <ul class="split-list">
      <li>Resellers</li><li>Retailers</li><li>Dealers</li><li>Distributors</li><li>Referral partners</li><li>Wholesalers</li><li>Affiliates</li><li>Franchisees</li>
    </ul>
    <span class="btn">SIGN UP</span>
  </div>
</section>

<section class="band why">
  <div class="why-photo" role="img" aria-label="Hand holding a glowing laptop with floating email icons and a world map"></div>
  <div class="why-copy">
    <div class="why-title">WHY PICK RESELLING?</div>
    <div class="why-pre">Bringing Reseller Opportunities</div>
    <div class="why-big">TO THE MASSES</div>
    <ul class="why-list">
      <li>Personal requirement for a reseller base.</li>
      <li>Experienced reseller models that work.</li>
      <li>Building an effective virtual sales team.</li>
      <li>Helping SME's earn money for old rope.</li>
      <li>Easy to generate revenue for a minimal cost</li>
    </ul>
    <span class="btn">SEE PLANS</span>
  </div>
</section>

<section class="band growth">
  <div class="growth-title">FAST TRACK <span>GROWTH</span></div>
  <svg width="1200" height="585" viewBox="0 0 1200 585" font-family="Montserrat, Arial, sans-serif">
    <g font-size="15" font-weight="700">
      <text x="208" y="160" fill="#fff">RESELLERS</text><text x="305" y="160" fill="#fff">INCREASE IN SALES</text>
      <text x="208" y="182" fill="var(--chart-green)">10-20</text><text x="305" y="182" fill="var(--chart-green)">2 - 5 x increase in sales</text>
      <text x="208" y="204" fill="var(--chart-blue)">30-50</text><text x="305" y="204" fill="var(--chart-blue)">5 - 10 x increase in sales</text>
      <text x="208" y="226" fill="var(--purple)">50+</text><text x="305" y="226" fill="var(--purple)">10+ x increase in sales</text>
    </g>
    <line x1="190" y1="150" x2="190" y2="440" stroke="#888" stroke-width="1.5"/>
    <line x1="190" y1="440" x2="1040" y2="440" stroke="#888" stroke-width="1.5"/>
    <line x1="190" y1="440" x2="190" y2="455" stroke="#888"/><line x1="610" y1="440" x2="610" y2="455" stroke="#888"/><line x1="1010" y1="440" x2="1010" y2="455" stroke="#888"/>
    <text x="160" y="320" fill="#fff" font-size="14" font-weight="700" transform="rotate(-90 160 320)" text-anchor="middle">MONTHLY SALES</text>
    <g fill="#fff" font-size="11" font-weight="600">
      <text x="200" y="468">1 MONTH</text><text x="620" y="468">6 MONTH</text><text x="1020" y="468">1 YEAR</text>
    </g>
    <g fill="none" stroke-width="2.5">
      <polyline stroke="var(--purple)" points="190,439 323,349 427,264 512,242 597,213 700,230 803,213 906,230 1009,155"/>
      <polyline stroke="var(--chart-blue)" points="190,439 323,369 427,319 512,296 597,296 700,302 803,319 906,296 1009,272"/>
      <polyline stroke="var(--chart-green)" points="190,439 323,399 427,374 512,361 597,369 700,361 803,381 906,352 1009,332"/>
      <polyline stroke="var(--red)" points="190,439 323,434 427,424 512,406 597,419 700,401 803,419 906,393 1009,384"/>
    </g>
    <g>
      <g fill="var(--purple)"><circle cx="323" cy="349" r="4"/><circle cx="427" cy="264" r="4"/><circle cx="512" cy="242" r="4"/><circle cx="597" cy="213" r="4"/><circle cx="700" cy="230" r="4"/><circle cx="803" cy="213" r="4"/><circle cx="906" cy="230" r="4"/><circle cx="1009" cy="155" r="4"/></g>
      <g fill="var(--chart-blue)"><circle cx="323" cy="369" r="4"/><circle cx="427" cy="319" r="4"/><circle cx="512" cy="296" r="4"/><circle cx="597" cy="296" r="4"/><circle cx="700" cy="302" r="4"/><circle cx="803" cy="319" r="4"/><circle cx="906" cy="296" r="4"/><circle cx="1009" cy="272" r="4"/></g>
      <g fill="var(--chart-green)"><circle cx="323" cy="399" r="4"/><circle cx="427" cy="374" r="4"/><circle cx="512" cy="361" r="4"/><circle cx="597" cy="369" r="4"/><circle cx="700" cy="361" r="4"/><circle cx="803" cy="381" r="4"/><circle cx="906" cy="352" r="4"/><circle cx="1009" cy="332" r="4"/></g>
      <g fill="var(--red)"><circle cx="323" cy="434" r="4"/><circle cx="427" cy="424" r="4"/><circle cx="512" cy="406" r="4"/><circle cx="597" cy="419" r="4"/><circle cx="700" cy="401" r="4"/><circle cx="803" cy="419" r="4"/><circle cx="906" cy="393" r="4"/><circle cx="1009" cy="384" r="4"/></g>
    </g>
    <g font-size="11" font-weight="600">
      <text x="912" y="206" fill="var(--purple)" transform="rotate(-30 912 206)">50+ Resellers</text>
      <text x="912" y="281" fill="var(--chart-blue)" transform="rotate(-12 912 281)">30 - 50 Resellers</text>
      <text x="912" y="340" fill="var(--chart-green)" transform="rotate(-10 912 340)">10 - 20 Resellers</text>
      <text x="912" y="384" fill="var(--red)" transform="rotate(-5 912 384)">Without Resellers</text>
    </g>
    <text x="600" y="510" fill="#4a5656" font-size="11" text-anchor="middle">All trends are based on a small - medium sized business and are approximate indications on growth.</text>
  </svg>
</section>

<section class="band how">
  <div class="how-title"><span>HOW</span> IT WORKS</div>
  <div class="flow merchant-flow">
    <span class="bullet"></span>MERCHANTS<span class="arrow">&#10132;</span>PAYMENT<span class="arrow">&#10132;</span>LISTING<span class="arrow">&#10132;</span>PROMOTE
    <span class="pricing">PRICING PLAN</span>
  </div>
  <div class="flow reseller-flow">
    <span class="bullet"></span>RESELLERS<span class="arrow">&#10132;</span>REGISTER<span class="arrow">&#10132;</span>SEARCH<span class="arrow">&#10132;</span>EARN
    <span class="pricing">PRICING PLAN</span>
  </div>
  <div class="shadow"></div>
</section>

<nav class="band footer-nav">
  <span class="active">HOME</span><span>RESELLERS</span><span>MERCHANTS</span><span>BUSINESS LISTINGS</span><span class="pill">SIGN-UP</span>
</nav>

<footer class="band site-footer">
  <div class="footer-brand"><span class="brand-dot"></span>tradeyourgoods</div>
  <p class="footer-blurb">Trade Your Goods connects merchants who want their products resold with resellers looking for the right products to sell. Merchants list their business and products, resellers search by industry or area, and both sides build lasting partnerships. We only charge a simple monthly subscription and take no share of the deals you make together through our marketplace.</p>
  <div class="copyright">Copyright © 2014-2015 Trade Your Goods Inc. All rights reserved.</div>
  <div class="socials"><span></span><span></span><span></span><span></span></div>
  <div class="legal"><span>Terms of use</span><span>Privacy Policy</span><span>Get Registered</span></div>
</footer>

</body>
</html>
```